Tervolan Pty Ltd professional business card

A professional business card template using the colours from the supplied logo.
Clean crisp lines while, Modern while not being over the top.

Target Market(s)

Construction, commerical and industrial

Industry/Entity Type

Communications

Contact Information for Business Card

For a Communications, IT, Optical fibre installation company

Colors
37b8a4

```html
<!DOCTYPE html>
<html lang="en">
<head>
<meta charset="utf-8">
<title>Tervolan Pty Ltd – Business Card</title>
<link href="https://fonts.googleapis.com/css2?family=Arimo:wght@400;700&display=swap" rel="stylesheet">
<style>
  :root {
    --teal: #1697a6;
    --teal-light: #37b8a4;
    --grey: #6d6e71;
    --ink: #333333;
    --paper: #ffffff;
    --backdrop: #2a2a2c;
  }
  * { margin: 0; padding: 0; box-sizing: border-box; }
  html, body {
    width: 1200px; height: 900px; overflow: hidden;
    background: var(--backdrop);
    font-family: "Arimo", Arial, sans-serif;
  }
  .card {
    position: absolute;
    width: 540px; height: 310px;
    background: var(--paper);
    overflow: hidden;
    box-shadow: 0 10px 30px rgba(0,0,0,.45);
  }
  .card--front { left: 90px; top: 110px; }
  .card--back { left: 570px; top: 470px; }

  .brand {
    display: flex; align-items: center; gap: 10px;
    color: var(--grey); font-weight: 700; letter-spacing: 1px;
  }
  .brand__mark { background: var(--teal); flex: none; }

  .card--front .brand {
    position: absolute; left: 0; right: 0; top: 118px;
    justify-content: center; font-size: 46px;
  }
  .card--front .brand__mark { width: 30px; height: 30px; }
  .card--front .site {
    position: absolute; left: 0; right: 0; top: 206px;
    text-align: center; font-size: 13px; letter-spacing: 4px; color: var(--ink);
  }

  .card__wave { position: absolute; inset: 0; width: 100%; height: 100%; }
  .card--back .brand {
    position: absolute; left: 26px; top: 50px; font-size: 38px;
  }
  .card--back .brand__mark { width: 24px; height: 24px; }
  .person {
    position: absolute; right: 34px; top: 26px; text-align: right;
  }
  .person__name { color: var(--teal); font-weight: 700; font-size: 20px; }
  .person__role { color: var(--ink); font-size: 12px; margin-top: 2px; }

  .contact {
    position: absolute; left: 30px; bottom: 20px;
    color: var(--paper); font-size: 13px; line-height: 17px; list-style: none;
  }
  .contact li { display: flex; align-items: center; gap: 7px; }
  .contact .address { margin-bottom: 4px; display: block; }
  .contact svg { width: 11px; height: 11px; flex: none; }
  .card--back .site {
    position: absolute; right: 30px; bottom: 80px;
    color: var(--paper); font-size: 14px;
  }
</style>
</head>
<body>
  <section class="card card--front">
    <div class="brand"><span class="brand__mark"></span>TERVOLAN</div>
    <p class="site">www.tervolan.com</p>
  </section>

  <section class="card card--back">
    <svg class="card__wave" viewBox="0 0 540 310" preserveAspectRatio="none" aria-hidden="true">
      <path d="M0,150 C120,112 280,102 400,98 C470,95 515,88 540,78 L540,310 L0,310 Z" fill="var(--grey)"/>
      <path d="M0,163 C120,125 280,115 400,111 C470,108 515,101 540,92 L540,310 L0,310 Z" fill="var(--teal)"/>
      <path d="M320,97 C410,92 490,82 540,64 L540,70 C490,88 410,95 320,97 Z" fill="var(--teal)"/>
    </svg>
    <div class="brand"><span class="brand__mark"></span>TERVOLAN</div>
    <div class="person">
      <p class="person__name">Daniel Hart</p>
      <p class="person__role">President</p>
    </div>
    <p class="site">www.tervolan.com</p>
    <ul class="contact">
      <li class="address">48b Kelvin Grove Road<br>Fulham, London SW6 4RT</li>
      <li><svg viewBox="0 0 12 12"><path d="M2 1h3l1 3-2 1a7 7 0 0 0 3 3l1-2 3 1v3c-6 0-10-4-10-9z" fill="#fff"/></svg>020 7946 0321</li>
      <li><svg viewBox="0 0 12 12"><rect x="3" y="0.5" width="6" height="11" rx="1" fill="none" stroke="#fff"/><circle cx="6" cy="9.5" r=".8" fill="#fff"/></svg>020 7946 0321</li>
      <li><svg viewBox="0 0 12 12"><rect x="1" y="5" width="10" height="5" fill="#fff"/><rect x="3" y="1" width="6" height="4" fill="none" stroke="#fff"/></svg>020 7946 0321</li>
      <li><svg viewBox="0 0 12 12"><rect x="0.5" y="2.5" width="11" height="7" fill="none" stroke="#fff"/><path d="M1 3l5 4 5-4" fill="none" stroke="#fff"/></svg>d.hart@tervolan.com</li>
    </ul>
  </section>
</body>
</html>
```